LINGERIE WEBSHOP - Velora casa

We are looking for design and layout design for our webshop. We are company that sells lingerie and other connected textile products liki payamas and etc..
Our website will have approx 500 different products within 2 main catogories Woman/Man) and approx. 10 subcategories
Here is what we expect form design:
-Color pallete should be black and white (if you wish you can add some accent color)
-we want to leave feeling to customers of good quality products towards to luxury
-UX should be simple. Feel free to suggest layout
-frontpage layout, product list layout, product description layout, blog layout
-responsive design, compatible with smartphone

Target Market(s)

woman buying for themself, man buying for woman

Industry/Entity Type

Lingerie

Logo Text

VELORA CASA

Number of Pages Required

4 page

Font styles to use
Sans Serif
Decorative

Requirements
Must have
• simple UX
Nice to have
• difference for sexy/luxury lingerie and daily/cozy lingerie
Should not have
• cheap feel, unreliable

```html
<!DOCTYPE html>
<html lang="en">
<head>
<meta charset="utf-8">
<title>Velora casa — Contact Us</title>
<link rel="stylesheet" href="https://fonts.googleapis.com/css2?family=Playfair+Display:wght@400;700;900&family=Poppins:wght@300;400;500;600&display=swap">
<style>
:root{
  --ink:#0b0b0b;
  --dark:#1c1c1c;
  --white:#ffffff;
  --muted:#9a9a9a;
  --line:#e3e3e3;
  --soft:#f7f7f7;
  --text:#333333;
  --accent:#d33a2c;
}
*{box-sizing:border-box;margin:0;padding:0}
html,body{width:1200px;height:2282px;overflow:hidden;background:var(--white)}
body{position:relative;font-family:'Poppins',sans-serif;color:var(--text)}
.abs{position:absolute}

.hero{left:0;top:0;width:1200px;height:357px;background:radial-gradient(ellipse at 50% 40%,#2b2b2b,#141414 75%)}
.brand{left:118px;top:28px;color:var(--white);font-weight:300;letter-spacing:1px;font-size:24px;line-height:1}
.brand small{display:block;font-size:11px;letter-spacing:2px;text-align:center;margin-bottom:6px;color:#ddd}
.nav{left:549px;top:39px;display:flex;gap:33px;color:var(--white);font-size:12.5px;font-weight:500}
.nav span svg{vertical-align:middle;margin-left:3px}
.iconbtn{top:28px;width:40px;height:40px;border:1.5px solid var(--white);border-radius:50%;display:flex;align-items:center;justify-content:center}
.badge{position:absolute;top:-4px;right:-6px;width:16px;height:16px;border-radius:50%;background:var(--white);color:var(--ink);font-size:9px;font-weight:600;display:flex;align-items:center;justify-content:center}
.hero-title{left:0;width:1200px;top:176px;text-align:center;color:var(--white);font-family:'Playfair Display',serif;font-size:54px;font-weight:700;line-height:70px}
.crumb{left:0;width:1200px;top:264px;text-align:center;color:#aaa;font-size:12px}
.crumb b{color:#ccc;font-weight:600}

.card{top:408px;width:295px;height:105px;border:1px solid var(--line);padding:26px 26px}
.card h3{font-family:'Playfair Display',serif;font-weight:700;font-size:20px;color:var(--ink)}
.card p{font-size:12.5px;margin-top:10px;color:var(--ink)}
.card svg{position:absolute;right:26px;top:28px}

.intro{left:0;width:1200px;top:565px;text-align:center;font-family:'Playfair Display',serif;font-size:29px;color:var(--ink);line-height:43px}
.intro b{font-weight:700}
.rule{left:560px;top:661px;width:80px;height:3px;background:var(--ink)}
.lead{left:0;width:1200px;top:688px;text-align:center;font-size:14.5px;color:var(--ink)}

.field{border:1px solid var(--line);height:39px;padding:12px 13px;font-size:11.5px;color:#777}
.send{left:150px;top:1026px;width:900px;height:39px;background:var(--ink);color:var(--white);font-size:11.5px;font-weight:500;display:flex;align-items:center;justify-content:center}

.map{left:0;top:1129px;width:1200px;height:317px;background:linear-gradient(160deg,#ececec,#e4e6e3 55%,#f1ecdc)}
.map-pin{left:590px;top:1256px}

.feat{top:1446px;width:300px;height:156px;background:var(--soft);border-right:1px solid #e8e8e8;padding:26px 37px}
.feat h4{font-family:'Playfair Display',serif;font-weight:400;font-size:26px;color:var(--ink);display:inline-block;border-bottom:2px solid #ddd;line-height:1.1}
.feat h4 b{font-weight:700}
.feat p{font-size:13px;line-height:18px;margin-top:18px;color:#333}

.dark{left:0;top:1602px;width:1200px;height:616px;background:var(--ink)}
.news-title{left:0;width:1200px;top:1655px;text-align:center;color:var(--white);font-family:'Playfair Display',serif;font-weight:900;font-size:54px}
.news-text{left:0;width:1200px;top:1742px;text-align:center;color:var(--white);font-size:14.5px;font-weight:500}
.news-input{left:423px;top:1789px;width:355px;height:48px;border:1.5px solid var(--white);border-radius:24px;color:#ddd;font-size:15px;padding:13px 25px;display:flex;justify-content:space-between}

.foot-brand{left:37px;top:1974px;color:var(--white);font-family:'Playfair Display',serif;font-size:32px;font-weight:700}
.foot-tag{left:37px;top:2021px;color:var(--white);font-size:13.5px}
.foot-rule{left:37px;top:2053px;width:225px;height:1px;background:#333}
.social{top:2078px;width:16px;height:16px;border-radius:50%;border:2px solid var(--white)}
.col{top:1967px}
.col h5{font-family:'Playfair Display',serif;font-size:20px;color:var(--white);font-weight:400;margin-bottom:18px}
.col h5 b{font-weight:700}
.col li{list-style:none;color:#aaa;font-size:13.5px;line-height:27px}

.bottom{left:0;top:2218px;width:1200px;height:64px;background:var(--white)}
.copy{left:37px;top:2243px;font-size:13px;color:var(--ink)}
.pay{top:2236px;width:60px;height:34px;background:#f0f0f0;border-radius:3px;font-size:11px;font-weight:600;color:#444;display:flex;align-items:center;justify-content:center}
</style>
</head>
<body>

<header class="abs hero"></header>
<div class="abs brand"><small>— est. 1998 —</small>VELORA CASA</div>
<nav class="abs nav">
  <span>HOME</span>
  <span>WOMEN<svg width="10" height="6" viewBox="0 0 10 6"><path d="M1 1l4 4 4-4" stroke="#fff" fill="none" stroke-width="1.3"/></svg></span>
  <span>MEN<svg width="10" height="6" viewBox="0 0 10 6"><path d="M1 1l4 4 4-4" stroke="#fff" fill="none" stroke-width="1.3"/></svg></span>
  <span>TRENDING</span>
  <span>CONTACT</span>
</nav>
<div class="abs iconbtn" style="left:970px">
  <svg width="16" height="14" viewBox="0 0 16 14"><path d="M8 13S1 8.5 1 4.5A3.3 3.3 0 0 1 8 3a3.3 3.3 0 0 1 7 1.5C15 8.5 8 13 8 13z" fill="none" stroke="#fff" stroke-width="1.3"/></svg>
  <span class="badge">1</span>
</div>
<div class="abs iconbtn" style="left:1029px">
  <svg width="16" height="14" viewBox="0 0 16 14"><path d="M1 1h2.5l2 8h8l1.5-6H4.5" fill="none" stroke="#fff" stroke-width="1.3"/><circle cx="6.5" cy="12" r="1.2" fill="#fff"/><circle cx="12.5" cy="12" r="1.2" fill="#fff"/></svg>
  <span class="badge">3</span>
</div>
<h1 class="abs hero-title">Contact Us</h1>
<div class="abs crumb">VELORA CASA &nbsp;&gt;&nbsp; <b>CONTACT US</b></div>

<section class="abs card" style="left:131px">
  <h3>Support</h3><p>(+01) 5 8821 4036</p>
  <svg width="50" height="50" viewBox="0 0 50 50"><path d="M8 4l9 0 4 11-6 4c3 7 8 12 15 15l4-6 11 4v9c0 3-3 5-6 5C20 45 5 30 4 10c0-3 2-6 4-6z" fill="none" stroke="#ddd" stroke-width="1.5"/></svg>
</section>
<section class="abs card" style="left:452px">
  <h3>E-Mail</h3><p>hello@veloracasa.com</p>
  <svg width="50" height="50" viewBox="0 0 50 50"><path d="M2 20L25 4l23 16v27H2z M2 20l23 16 23-16" fill="none" stroke="#ddd" stroke-width="1.5"/></svg>
</section>
<section class="abs card" style="left:773px">
  <h3>Adress</h3><p>742 Marlow Street</p>
  <svg width="56" height="44" viewBox="0 0 56 44"><path d="M2 6l17-4 18 4 17-4v36l-17 4-18-4-17 4z M19 2v36 M37 6v36" fill="none" stroke="#ddd" stroke-width="1.5"/></svg>
</section>

<div class="abs intro"><b>Let us know what you have in mind,</b><br>and we’ll get back to you in an instant!</div>
<div class="abs rule"></div>
<p class="abs lead">Lorem Ipsum is simply dummy text of the printing and typesetting industry.</p>

<div class="abs field" style="left:150px;top:759px;width:438px">Your Name</div>
<div class="abs field" style="left:612px;top:759px;width:438px">E-Mail adress</div>
<div class="abs field" style="left:150px;top:811px;width:438px">Subject</div>
<div class="abs field" style="left:612px;top:811px;width:438px">Phone Number</div>
<div class="abs field" style="left:150px;top:864px;width:900px;height:149px">Your Message</div>
<div class="abs send">Send Message</div>

<div class="abs map" role="img" aria-label="Street map showing the shop location with a red marker"></div>
<svg class="abs map-pin" width="20" height="28" viewBox="0 0 20 28"><path d="M10 27C10 27 1 15 1 9.5a9 9 0 0 1 18 0C19 15 10 27 10 27z" fill="#d33a2c"/><circle cx="10" cy="9.5" r="3" fill="#8f1f16"/></svg>

<div class="abs feat" style="left:0"><h4>Free <b>Delivery</b></h4><p>Lorem Ipsum is simply dummy text of the printing and typesetting industry.</p></div>
<div class="abs feat" style="left:300px"><h4><b>Safe</b> Shopping</h4><p>Lorem Ipsum is simply dummy text of the printing and typesetting industry.</p></div>
<div class="abs feat" style="left:600px"><h4>Easy <b>Refunded</b></h4><p>Lorem Ipsum is simply dummy text of the printing and typesetting industry.</p></div>
<div class="abs feat" style="left:900px;border-right:none"><h4>7/24 <b>Support</b></h4><p>Lorem Ipsum is simply dummy text of the printing and typesetting industry.</p></div>

<div class="abs dark"></div>
<h2 class="abs news-title">Newsletter</h2>
<p class="abs news-text">Subscribe to our newsletter to receive weekly news, updates, special offers and exclusive sorts discounts.</p>
<div class="abs news-input"><span>Enter your e-mail address</span>
  <svg width="16" height="16" viewBox="0 0 16 16" style="margin-top:3px"><path d="M2 8h12M9 3l5 5-5 5" fill="none" stroke="#fff" stroke-width="1.6"/></svg>
</div>

<div class="abs foot-brand">Velora casa</div>
<div class="abs foot-tag">20 years with you</div>
<div class="abs foot-rule"></div>
<span class="abs social" style="left:46px" aria-label="Social link"></span>
<span class="abs social" style="left:85px" aria-label="Social link"></span>
<span class="abs social" style="left:125px" aria-label="Social link"></span>
<span class="abs social" style="left:163px" aria-label="Social link"></span>
<span class="abs social" style="left:202px" aria-label="Social link"></span>

<div class="abs col" style="left:337px"><h5>for <b>Women</b></h5><ul><li>Body</li><li>Pants</li><li>Bras</li><li>Swimwear</li><li>T-Shirts</li></ul></div>
<div class="abs col" style="left:537px"><h5>for <b>Men</b></h5><ul><li>Body</li><li>Pants</li><li>Bras</li><li>Swimwear</li><li>T-Shirts</li></ul></div>
<div class="abs col" style="left:737px"><h5>Quick <b>Links</b></h5><ul><li>Track Your Order</li><li>Delivery</li><li>Returns</li><li>Cookie Policy</li><li>Privacy Policy</li></ul></div>
<div class="abs col" style="left:937px"><h5>Our <b>Company</b></h5><ul><li>About Us</li><li>Contact Us</li><li>Terms of Use</li><li>Terms of Purchase</li><li>Security Payment</li></ul></div>

<div class="abs bottom"></div>
<div class="abs copy">©2020 Velora casa. All rights reserved</div>
<div class="abs pay" style="left:907px">Paylo</div>
<div class="abs pay" style="left:973px">Cardia</div>
<div class="abs pay" style="left:1039px">Tendra</div>
<div class="abs pay" style="left:1105px">Orbex</div>

</body>
</html>
```